Business Card Redesign

We are looking for a designer to redesign our current business card (attached below). The logo itself will not change but the look and feel of the rest of the card needs to be freshened up. The text on the back of the card is to be changed to:
Strategic Alignment
Leadership and Coaching
Sales Force Development
Sales Talent Acquisition
Emotional Intelligence Facilitation & Certification
Guest speaking

The byline needs to be retained "Genuine Connections... Confident futures" along with the logo.

All up we will need business cards laid out for 6 people.

Also, once we receive a design that we are happy with we will need the branding to be continued through onto other documentation such as workbook cover pages, email signatures etc and will negotiate with the successful designer on this future piece of work.

Please review our website for more of an idea of who we are, our style, and what we do. www.brightoakpartners.com.au and www.heartwisecapability-hw-c.com.au.

Thank you for your interest.

```html
<!DOCTYPE html>
<html lang="en">
<head>
<meta charset="utf-8">
<title>Bright Oak Partners – Business Card, Option 3</title>
<link rel="stylesheet" href="https://fonts.googleapis.com/css2?family=Jost:wght@300;400;500&display=swap">
<style>
  :root {
    --ink-deep: #1212e0;
    --ink-sky: #2a8cff;
    --ink-grey: #666666;
    --label: #111111;
    --card-edge: #333333;
    --paper: #ffffff;
  }
  * { box-sizing: border-box; margin: 0; padding: 0; }
  html, body {
    width: 938px;
    height: 1200px;
    overflow: hidden;
    background: var(--paper);
    font-family: "Jost", "Futura", sans-serif;
  }
  .sheet { position: relative; width: 938px; height: 1200px; }
  .option-label {
    position: absolute;
    top: 0;
    left: 0;
    width: 100%;
    text-align: center;
    font-weight: 300;
    font-size: 28px;
    line-height: 1;
    color: var(--label);
  }
  .card {
    position: absolute;
    left: 0;
    width: 938px;
    height: 536px;
    border: 1px solid var(--card-edge);
    background: var(--paper);
  }
  .card--front { top: 54px; }
  .card--back { top: 663px; }
  .line {
    position: absolute;
    left: 0;
    width: 100%;
    text-align: center;
    line-height: 1;
    font-weight: 300;
    white-space: nowrap;
  }
  .holder-name { top: 49px; font-size: 37px; font-weight: 400; color: var(--ink-deep); }
  .holder-title { top: 93px; font-size: 25px; color: var(--ink-sky); }
  .brand {
    position: absolute;
    top: 380px;
    left: 0;
    width: 100%;
    display: flex;
    justify-content: center;
    align-items: center;
    gap: 14px;
  }
  .brand-dot { width: 34px; height: 34px; border-radius: 50%; background: var(--ink-sky); }
  .brand-name { font-size: 50px; font-weight: 500; line-height: 1; color: var(--ink-deep); }
  .tagline { top: 487px; font-size: 24px; color: var(--ink-grey); }
  .service { font-size: 28px; }
  .service--sky { color: var(--ink-sky); }
  .service--deep { color: var(--ink-deep); }
  .divider {
    position: absolute;
    top: 382px;
    left: 74px;
    width: 790px;
    height: 2px;
    background: var(--ink-deep);
  }
  .contact { font-size: 27px; }
  .contact--phone { top: 420px; font-size: 26px; font-weight: 400; color: var(--ink-deep); }
  .contact--web { top: 452px; color: var(--ink-sky); }
  .contact--address { top: 494px; font-weight: 400; color: var(--ink-sky); font-size: 26px; }
</style>
</head>
<body>
<main class="sheet">
  <p class="option-label">Option 3</p>

  <section class="card card--front" aria-label="Card front">
    <h1 class="line holder-name">Tara Lindqvist</h1>
    <p class="line holder-title">Client Services Manager</p>
    <div class="brand">
      <span class="brand-dot" aria-hidden="true"></span>
      <span class="brand-name">Bright Oak Partners</span>
    </div>
    <p class="line tagline">Genuine Connections... Confident futures</p>
  </section>

  <section class="card card--back" aria-label="Card back">
    <p class="line service service--sky" style="top:54px">Strategic Alignment</p>
    <p class="line service service--deep" style="top:107px">Leadership and Coaching</p>
    <p class="line service service--sky" style="top:160px">Sales Force Development</p>
    <p class="line service service--deep" style="top:213px">Sales Talent Acquisition</p>
    <p class="line service service--sky" style="top:266px">Emotional Intelligence Facilitation and Certification</p>
    <p class="line service service--deep" style="top:319px">Guest speaking</p>
    <div class="divider" aria-hidden="true"></div>
    <p class="line contact contact--phone">Phone : + 613 9555 4182</p>
    <p class="line contact contact--web">tara@brightoakpartners.com.au I www.brightoakpartners.com.au</p>
    <p class="line contact contact--address">Suite 2.04, 417 Kingsway Rd, Cheltenham, Australia - 3192</p>
  </section>
</main>
</body>
</html>
```